Boutique Technology Consultancy specialising is Electronic and physical security

We need to redo our existing outdated website. For your reference the link www.brivo.com.au

```html
<!DOCTYPE html>
<html lang="en">
<head>
<meta charset="utf-8">
<title>Qorvane Services — Technology Consulting</title>
<link rel="stylesheet" href="https://fonts.googleapis.com/css2?family=Tenor+Sans&family=Poppins:wght@400;500;600&family=Cinzel:wght@400&display=swap">
<style>
:root{
  --page:#1c0103;
  --red:#b5121b;
  --white:#ffffff;
  --soft:#e9d6d6;
  --muted:#c9a9aa;
  --card:#3a0306;
  --photo-a:#7a2a2c;
  --photo-b:#2e0608;
}
*{margin:0;padding:0;box-sizing:border-box}
html,body{width:1200px;height:4895px;overflow:hidden;background:var(--page)}
body{position:relative;font-family:"Poppins",sans-serif;color:var(--white)}
.abs{position:absolute}
.heading{font-family:"Tenor Sans",sans-serif;font-weight:400;color:var(--white)}
.photo{position:absolute;background:linear-gradient(150deg,var(--photo-a),var(--photo-b))}
.body-text{font-size:11px;line-height:24px;color:var(--soft)}
.pill{position:absolute;display:flex;align-items:center;justify-content:space-between;border-radius:20px;padding:0 4px 0 30px;font-size:11px;font-weight:500}
.pill .dot{width:26px;height:26px;border-radius:50%;display:flex;align-items:center;justify-content:center}
.pill-light{background:var(--white);color:#3a0306}
.pill-light .dot{background:var(--red)}
.pill-red{background:var(--red);color:var(--white)}
.pill-red .dot{background:var(--white)}
.social{position:absolute;width:22px;height:22px;border-radius:50%;background:var(--white)}
.logo{font-family:"Tenor Sans",sans-serif;font-size:34px;letter-spacing:3px;color:var(--white)}

.hero{left:14px;top:0;width:1186px;height:675px;background:linear-gradient(120deg,#4b0509,#2c0204)}
.nav a{position:absolute;top:44px;font-size:11px;color:var(--white);text-decoration:none}
.hero-title{left:120px;top:152px;font-size:56px;line-height:61px}
.hero-rule{left:120px;top:357px;width:372px;height:1px;background:var(--muted)}

.check{position:absolute;display:flex;align-items:center;gap:16px;font-size:10px;color:var(--soft)}
.check i{width:22px;height:22px;border-radius:50%;background:var(--white);display:flex;align-items:center;justify-content:center}
.stat-num{font-family:"Tenor Sans",sans-serif;font-size:31px}
.stat-label{font-size:19px}

.band{left:8px;width:1184px;background:radial-gradient(ellipse at 75% 30%,#5c080c,#3a0306 70%)}
.divider{width:1px;background:var(--muted)}

.svc-card{position:absolute;top:1675px;width:305px;height:293px}
.why-card{position:absolute;top:2373px;width:292px;height:400px;background:var(--card);box-shadow:0 10px 30px rgba(0,0,0,.4)}
.why-card .photo{left:0;top:0;width:292px;height:213px}
.why-card .icon{position:absolute;left:194px;top:194px;width:70px;height:70px;background:var(--page);display:flex;align-items:center;justify-content:center}
.why-card h3{position:absolute;left:28px;top:270px;font-size:14px;font-weight:600;line-height:21px}
.why-card p{position:absolute;left:28px;top:320px;width:240px;font-size:9.5px;line-height:21px;color:var(--soft)}

.member-name{position:absolute;width:293px;text-align:center;font-family:"Cinzel",serif;font-size:18px}
.member-role{position:absolute;width:293px;text-align:center;font-size:13px;color:var(--soft)}

.blog-card{position:absolute;top:3872px;width:304px;height:443px;background:var(--card)}
.blog-card .photo{left:55px;top:-46px;width:249px;height:247px}
.blog-card .date{position:absolute;left:16px;top:164px;transform:rotate(-90deg);transform-origin:left top;font-family:"Cinzel",serif;font-size:20px;white-space:nowrap}
.blog-card h3{position:absolute;left:55px;top:244px;font-size:14px;font-weight:600;line-height:20px}
.blog-card p{position:absolute;left:55px;top:298px;width:230px;font-size:9.5px;line-height:21px;color:var(--soft)}
.blog-card .more{position:absolute;left:55px;top:376px;font-size:9.5px;font-weight:600;display:flex;align-items:center;gap:10px}

.footer{left:0;top:4430px;width:1200px;height:465px;background:linear-gradient(160deg,#3a0306,#150002 60%)}
.qlink{position:absolute;right:968px;font-size:12px;color:var(--soft)}
.contact-icon{position:absolute;left:880px;width:38px;height:38px;border-radius:50%;background:var(--white);display:flex;align-items:center;justify-content:center}
.contact-text{position:absolute;left:932px;font-size:13px;line-height:23px;color:var(--soft)}
</style>
</head>
<body>

<section class="abs hero"></section>
<div class="photo" role="img" aria-label="Portrait of a consultant seated in a studio, warm red tone" style="left:0;top:0;width:1200px;height:675px;clip-path:polygon(380px 675px,1200px 0,1200px 675px);"></div>

<div class="abs logo" style="left:124px;top:30px">QORVANE</div>
<nav class="nav">
  <a style="left:338px;font-weight:600">Home</a>
  <a style="left:406px">About Us</a>
  <a style="left:493px">Our Services</a>
  <a style="left:599px">Our Team</a>
  <a style="left:689px">Experience</a>
</nav>
<div class="pill pill-red" style="left:787px;top:34px;width:140px;height:34px">Contact Us<span class="dot"><svg width="12" height="12" viewBox="0 0 12 12"><path d="M2 6h8M7 3l3 3-3 3" stroke="#b5121b" stroke-width="1.6" fill="none"/></svg></span></div>

<h1 class="abs heading hero-title">Your Technology<br>Projects Made<br>Easy</h1>
<div class="abs hero-rule"></div>
<p class="abs body-text" style="left:120px;top:376px;width:360px">Qorvane Services Was Established In 2016 By Rowan Hale To Provide Technology Consulting Services To Corporate And Government Clients With A Focus On</p>
<div class="pill pill-light" style="left:114px;top:481px;width:142px;height:34px">Read More<span class="dot"><svg width="12" height="12" viewBox="0 0 12 12"><path d="M2 6h8M7 3l3 3-3 3" stroke="#fff" stroke-width="1.6" fill="none"/></svg></span></div>
<div class="abs" style="left:114px;top:563px;font-size:11px;font-weight:500">Follow Us On</div>
<span class="social" style="left:114px;top:600px" aria-label="Social link"></span>
<span class="social" style="left:144px;top:600px" aria-label="Social link"></span>
<span class="social" style="left:174px;top:600px" aria-label="Social link"></span>
<span class="social" style="left:204px;top:600px" aria-label="Social link"></span>

<h2 class="abs heading" style="left:120px;top:862px;font-size:47px">About Us</h2>
<p class="abs body-text" style="left:120px;top:934px;width:310px">Qorvane Is A Privately Owned Independent Consultancy 100% Dedicated To Customer Satisfaction. With Experience In A Range Of Technologies Such As Internet Of Things, Security Systems, Wi-Fi, Building Services Networks, Control Centres And Smart Buildings, Our Services Include:</p>
<div class="check" style="left:120px;top:1105px"><i><svg width="11" height="11" viewBox="0 0 11 11"><path d="M2 5.5l2.5 2.5L9 3" stroke="#3a0306" stroke-width="1.8" fill="none"/></svg></i>Technology Audits</div>
<div class="check" style="left:291px;top:1105px"><i><svg width="11" height="11" viewBox="0 0 11 11"><path d="M2 5.5l2.5 2.5L9 3" stroke="#3a0306" stroke-width="1.8" fill="none"/></svg></i>Technology Roadmaps</div>
<div class="check" style="left:120px;top:1145px"><i><svg width="11" height="11" viewBox="0 0 11 11"><path d="M2 5.5l2.5 2.5L9 3" stroke="#3a0306" stroke-width="1.8" fill="none"/></svg></i>Technology Designs</div>
<div class="check" style="left:291px;top:1145px"><i><svg width="11" height="11" viewBox="0 0 11 11"><path d="M2 5.5l2.5 2.5L9 3" stroke="#3a0306" stroke-width="1.8" fill="none"/></svg></i>Technology Procurement</div>
<div class="check" style="left:120px;top:1187px"><i><svg width="11" height="11" viewBox="0 0 11 11"><path d="M2 5.5l2.5 2.5L9 3" stroke="#3a0306" stroke-width="1.8" fill="none"/></svg></i>Technology Project Management</div>
<div class="pill pill-red" style="left:120px;top:1248px;width:142px;height:36px">Learn More<span class="dot"><svg width="12" height="12" viewBox="0 0 12 12"><path d="M2 6h8M7 3l3 3-3 3" stroke="#b5121b" stroke-width="1.6" fill="none"/></svg></span></div>

<div class="photo" role="img" aria-label="Two colleagues in business attire reviewing a tablet" style="left:502px;top:782px;width:417px;height:551px;background:linear-gradient(160deg,#8a3a2e,#3b0b0b)"></div>
<div class="abs" style="left:867px;top:730px;width:104px;height:104px;border-radius:50%;background:var(--white);box-shadow:0 0 0 8px rgba(255,255,255,.25);display:flex;align-items:center;justify-content:center"><svg width="20" height="20" viewBox="0 0 20 20"><path d="M6 3l11 7-11 7z" fill="#1c0103"/></svg></div>

<div class="abs" style="left:949px;top:880px"><div class="stat-num">130+</div><div class="stat-label">Project Done</div></div>
<div class="abs" style="left:949px;top:1022px"><div class="stat-num">263 +</div><div class="stat-label">Experience Team</div></div>
<div class="abs" style="left:949px;top:1162px"><div class="stat-num">25+</div><div class="stat-label">Awards Winning</div></div>

<section class="abs band" style="top:1449px;height:706px"></section>
<h2 class="abs heading" style="left:120px;top:1560px;font-size:47px">Our Services</h2>
<div class="abs divider" style="left:561px;top:1560px;height:57px"></div>
<p class="abs body-text" style="left:738px;top:1555px;width:360px">Lorem Ipsum Is Simply Dummy Text Of The Printing And Typesetting Industry. Lorem Ipsum Has Been The Industry's Standard Dummy Text Ever Since The 1500s</p>
<div class="svc-card photo" role="img" aria-label="Two consultants in suits talking" style="left:120px"></div>
<div class="abs" style="left:150px;top:1764px"><svg width="40" height="36" viewBox="0 0 40 36"><path d="M4 34V22M12 34V16M20 34V10M28 34V4M2 34h36" stroke="#fff" stroke-width="3" fill="none"/></svg></div>
<div class="abs" style="left:150px;top:1846px;font-size:24px;font-family:'Tenor Sans',sans-serif">Strategy</div>
<p class="abs" style="left:150px;top:1884px;width:150px;font-size:10px;line-height:21px;color:var(--soft)">Lorem Ipsum Is Simply Dummy Text Of The Printing And Typesetting Industry.</p>
<div class="abs" style="left:366px;top:1908px;width:28px;height:28px;border-radius:50%;border:1.5px solid #fff;display:flex;align-items:center;justify-content:center"><svg width="10" height="10" viewBox="0 0 10 10"><path d="M2 8l6-6M3 2h5v5" stroke="#fff" stroke-width="1.4" fill="none"/></svg></div>
<div class="svc-card photo" role="img" aria-label="Team meeting around a table" style="left:447px;background:linear-gradient(150deg,#c98f86,#5c1a1c)"></div>
<div class="svc-card photo" role="img" aria-label="Two professionals reviewing a tablet" style="left:774px;background:linear-gradient(150deg,#e6d4d6,#7a4f68)"></div>
<div class="pill pill-light" style="left:529px;top:2006px;width:142px;height:35px">Learn More<span class="dot"><svg width="12" height="12" viewBox="0 0 12 12"><path d="M2 6h8M7 3l3 3-3 3" stroke="#fff" stroke-width="1.6" fill="none"/></svg></span></div>

<h2 class="abs heading" style="left:0;top:2266px;width:1200px;text-align:center;font-size:47px">Why Choose Us</h2>
<article class="why-card" style="left:124px">
  <div class="photo" role="img" aria-label="Colleagues discussing documents at a desk" style="background:linear-gradient(150deg,#e9dcd3,#6b3a33)"></div>
  <div class="icon"><svg width="30" height="30" viewBox="0 0 30 30"><circle cx="11" cy="17" r="6" fill="none" stroke="#fff" stroke-width="3"/><circle cx="21" cy="9" r="4" fill="none" stroke="#fff" stroke-width="3"/></svg></div>
  <h3>Asset<br>Management</h3>
  <p>Lorem Ipsum is simply dummy text of the printing and typesetting industry. Lorem Ipsum has been the industry's.</p>
</article>
<article class="why-card" style="left:453px">
  <div class="photo" role="img" aria-label="Business team standing around a table" style="background:linear-gradient(150deg,#c9a48f,#4a2520)"></div>
  <div class="icon"><svg width="30" height="30" viewBox="0 0 30 30"><path d="M5 26V18M11 26V13M17 26V16M23 26V8M3 26h24M5 12l8-6 5 4 8-7" stroke="#fff" stroke-width="2.5" fill="none"/></svg></div>
  <h3>Property/Facilities<br>Management</h3>
  <p>Lorem Ipsum is simply dummy text of the printing and typesetting industry. Lorem Ipsum has been the industry's.</p>
</article>
<article class="why-card" style="left:783px">
  <div class="photo" role="img" aria-label="Two men working with a laptop in an office" style="background:linear-gradient(150deg,#d8d3d6,#5b4a55)"></div>
  <div class="icon"><svg width="30" height="30" viewBox="0 0 30 30"><circle cx="13" cy="9" r="5" fill="none" stroke="#fff" stroke-width="2.5"/><path d="M4 26c0-6 4-9 9-9" stroke="#fff" stroke-width="2.5" fill="none"/><circle cx="21" cy="21" r="4" fill="none" stroke="#fff" stroke-width="2.5"/></svg></div>
  <h3>Development And<br>Construction</h3>
  <p>Lorem Ipsum is simply dummy text of the printing and typesetting industry. Lorem Ipsum has been the industry's.</p>
</article>

<section class="abs band" style="top:2887px;height:713px"></section>
<h2 class="abs heading" style="left:120px;top:2998px;font-size:47px">Our Team</h2>
<div class="abs divider" style="left:534px;top:2998px;height:57px"></div>
<p class="abs body-text" style="left:738px;top:2993px;width:360px">Lorem Ipsum Is Simply Dummy Text Of The Printing And Typesetting Industry. Lorem Ipsum Has Been The Industry's Standard Dummy Text Ever Since The 1500s</p>

<div class="photo" role="img" aria-label="Portrait of a senior consultant" style="left:120px;top:3107px;width:293px;height:308px;background:linear-gradient(180deg,#5a3c3a,#1e0a0a)"></div>
<div class="member-name" style="left:120px;top:3335px">Glen Abbott</div>
<div class="member-role" style="left:120px;top:3364px">Principal Consultant</div>
<span class="abs" style="left:168px;top:3441px;width:40px;height:40px;border-radius:50%;background:#5a0a0e" aria-label="Social link"></span>
<span class="abs" style="left:220px;top:3441px;width:40px;height:40px;border-radius:50%;background:#5a0a0e" aria-label="Social link"></span>
<span class="abs" style="left:271px;top:3441px;width:40px;height:40px;border-radius:50%;background:#5a0a0e" aria-label="Social link"></span>
<span class="abs" style="left:322px;top:3441px;width:40px;height:40px;border-radius:50%;background:#5a0a0e" aria-label="Social link"></span>

<div class="photo" role="img" aria-label="Portrait of a principal consultant" style="left:453px;top:3107px;width:293px;height:308px;background:linear-gradient(180deg,#b0433a,#5a0f10)"></div>
<div class="member-name" style="left:453px;top:3446px">Rowan Hale</div>
<div class="member-role" style="left:453px;top:3474px">Principal Consultant</div>

<div class="photo" role="img" aria-label="Portrait of a senior consultant" style="left:787px;top:3107px;width:293px;height:308px;background:linear-gradient(180deg,#b0433a,#5a0f10)"></div>
<div class="member-name" style="left:787px;top:3446px">Marcus Trent</div>
<div class="member-role" style="left:787px;top:3474px">Senior Consultant</div>

<h2 class="abs heading" style="left:0;top:3710px;width:1200px;text-align:center;font-size:47px">Latest News &amp; Blog</h2>
<article class="blog-card" style="left:120px">
  <div class="photo" role="img" aria-label="Consultant writing at a laptop" style="background:linear-gradient(150deg,#d9cfcf,#4a3434)"></div>
  <div class="date">25-NOV-23</div>
  <h3>Lorem Ipsum Is Simply<br>Dummy Text</h3>
  <p>Lorem Ipsum is simply dummy text of the printing and typesetting industry. Lorem Ipsum has been the industry's.</p>
  <div class="more">Read More<svg width="30" height="6" viewBox="0 0 30 6"><path d="M0 3h28M25 0l3 3-3 3" stroke="#fff" fill="none"/></svg></div>
</article>
<article class="blog-card" style="left:447px">
  <div class="photo" role="img" aria-label="Group reviewing papers together" style="background:linear-gradient(150deg,#c6bcbf,#3e2e34)"></div>
  <div class="date">25-NOV-23</div>
  <h3>Lorem Ipsum Is Simply<br>Dummy Text</h3>
  <p>Lorem Ipsum is simply dummy text of the printing and typesetting industry. Lorem Ipsum has been the industry's.</p>
  <div class="more">Read More<svg width="30" height="6" viewBox="0 0 30 6"><path d="M0 3h28M25 0l3 3-3 3" stroke="#fff" fill="none"/></svg></div>
</article>
<article class="blog-card" style="left:774px">
  <div class="photo" role="img" aria-label="Colleagues working at a shared desk" style="background:linear-gradient(150deg,#dcd6d0,#4a3d36)"></div>
  <div class="date">25-NOV-23</div>
  <h3>Lorem Ipsum Is Simply<br>Dummy Text</h3>
  <p>Lorem Ipsum is simply dummy text of the printing and typesetting industry. Lorem Ipsum has been the industry's.</p>
  <div class="more">Read More<svg width="30" height="6" viewBox="0 0 30 6"><path d="M0 3h28M25 0l3 3-3 3" stroke="#fff" fill="none"/></svg></div>
</article>

<footer class="abs footer"></footer>
<div class="abs heading" style="left:120px;top:4540px;font-size:20px">Quick Links</div>
<div class="qlink" style="top:4590px">Home</div>
<div class="qlink" style="top:4626px">About Us</div>
<div class="qlink" style="top:4662px">Our Services</div>
<div class="qlink" style="top:4698px">Experience</div>
<div class="qlink" style="top:4734px">Our Team</div>
<div class="qlink" style="top:4770px">Contact Us</div>

<div class="abs logo" style="left:0;top:4550px;width:1114px;text-align:center">QORVANE</div>
<span class="abs" style="left:460px;top:4643px;width:38px;height:38px;border-radius:50%;background:var(--red)" aria-label="Social link"></span>
<span class="abs" style="left:510px;top:4643px;width:38px;height:38px;border-radius:50%;background:var(--white)" aria-label="Social link"></span>
<span class="abs" style="left:561px;top:4643px;width:38px;height:38px;border-radius:50%;background:var(--white)" aria-label="Social link"></span>
<span class="abs" style="left:612px;top:4643px;width:38px;height:38px;border-radius:50%;background:var(--white)" aria-label="Social link"></span>
<div class="abs" style="left:0;top:4732px;width:1114px;text-align:center;font-size:12px;color:var(--soft)">© Copyright 2023 <b style="color:#fff">Qorvane Services</b> . All rights reserved</div>
<div class="abs" style="left:0;top:4760px;width:1114px;text-align:center;font-size:12px;font-weight:600">Privacy Policy &nbsp; | &nbsp; Sitemap</div>

<div class="abs heading" style="left:879px;top:4540px;font-size:20px">Contact Us</div>
<div class="contact-icon" style="top:4605px"><svg width="14" height="16" viewBox="0 0 14 16"><path d="M7 15s5-5 5-9A5 5 0 002 6c0 4 5 9 5 9z" fill="#3a0306"/><circle cx="7" cy="6" r="2" fill="#fff"/></svg></div>
<div class="contact-text" style="top:4588px">Level 2, 118 Harbour<br>St, Melbourne VIC<br>3000</div>
<div class="contact-icon" style="top:4679px"><svg width="14" height="14" viewBox="0 0 14 14"><path d="M1 7l12-6-4 12-2-5z" fill="#3a0306"/></svg></div>
<div class="contact-text" style="top:4686px">hello@qorvane.com.au</div>
<div class="contact-icon" style="top:4746px"><svg width="14" height="14" viewBox="0 0 14 14"><path d="M3 1l3 3-2 2c1 2 2 3 4 4l2-2 3 3-2 2C6 13 1 8 1 3z" fill="#3a0306"/></svg></div>
<div class="contact-text" style="top:4753px">1300 555 014</div>

</body>
</html>
```